Kestrel Awards Brochure Design

We require a brochure design for ongoing marketing of our business / services.

Purpose - Informative brochure to inquire customers about the products and services we offer.

Brochure size – Bi Fold, Tri fold, or suggested format size

Aim- Corporate/business awards and products. We already have most sporting and scholastic business in the area and would like to target the corporate and businesses in and around the area focusing on employee recognition, achievement awards, etc. since these purchases bring in more revenue.

** Can get Pictures of products from our Website if need be:
Kestrelawards.example

About: We are a small private owned company located in the Lehigh valley of Pennsylvania and recently celebrated our 30 years in business. We offer a wide range of products and specialize in custom workmanship. Since we offer so many products for many different occasions, we need to make a brochure that isn’t condensed with our products. Just an informative brochure that will spark ideas and remind customers we are their one stop shop for business/corporate needs.

Possible Ideas-
Front page:
Kestrel Trophy & Awards
Logo
30 Years in Business
Slogan: Recognition at its best
About us Page:
Since 1983 our staff has been creating quality engraved awards, trophies, and plaques along with a full line of promotional products and embroidered apparel. We continue to offer top quality workmanship on a wide range of products and as always, you will receive our outstanding personal service.

Products

Recognition:
Trophies
Plaques
Certificates
Medals & Ribbons
Crystal, Glass, & Acrylic Awards

Business Needs:
Customized Stamps
Name Badges
Signs & Holders
Plastic Signage
Screen Printing & Embroidery
Advertising Specialties: Mugs, Pens, Magnets

Gifts:
Clocks
Frames
Key Chains
Desk Accessories
Artistic Glass Sculptures
Mugs, Glasses, Tumblers

Specialty:
Cast Bronze & Silver Tablets
Laser Engraving
Glass, Wood, Leather, Marble, Granite, Metal, & More.

Thousands of Choices!

Perfect Choice for:
Religious Awards
Secretary Gift
Scholastic Achievement
Athletic Milestones
Employee Awards
Executive Awards
Personalized Gifts
Corporate Awards
Golf Awards
Sales Awards
Achievement
Recognition

come in to visit our display room.
Kestrelawards.example

Rush Service Available
Friendly Customer Service
Fast Turn around
Free Proofs
Ship Anywhere in the US
Updates

We are looking for something more professional and eye catching. Please submit some new designs. Also updated the brief to make it a little easier. Again, We would like a tri fold brochure. The brochure must be informative and trigger the customers thoughts. Also would like a logo that says we have been in the business for 30 years! Ill extend the deadline for just a few more days. Thank you everyone.

Target Market(s)

Corporate and local business

Industry/Entity Type

Marketing

Requirements
Must have
• Hours of Operation:
Monday-Wedneday-Friday: 9am – 6pm
Tuesday- Thursday: 9am – 7pm
Saturday 9am – 4pm (May thru Aug: (9am - 2pm)
Location: 4182 Dorrance Mill Road, Easton PA 18045
Phone Number: 610-555-0147 Fax: 610-555-0193
Email: Sales@Kestrelawards.example
Should not have
• I need a brochure that is NOT going to just list the products and services.

```html
<!DOCTYPE html>
<html lang="en">
<head>
<meta charset="utf-8">
<title>Kestrel Trophy &amp; Awards – Tri-fold Inside</title>
<link rel="stylesheet" href="https://fonts.googleapis.com/css2?family=Arimo:wght@400;700&family=Didact+Gothic&family=Crimson+Text:wght@400;700&display=swap">
<style>
  :root {
    --green: #1f9e0b;
    --ink: #111111;
    --rule: #8a8a8a;
    --paper: #ffffff;
  }
  * { margin: 0; padding: 0; box-sizing: border-box; }
  html, body { width: 1200px; height: 927px; overflow: hidden; background: var(--paper); }
  .brochure { position: relative; width: 1200px; height: 927px; background: var(--paper); color: var(--ink); }

  .section-title {
    position: absolute;
    font-family: "Didact Gothic", "Century Gothic", sans-serif;
    font-weight: 400;
    font-size: 36px;
    color: var(--green);
    line-height: 1;
    padding-bottom: 4px;
    border-bottom: 1.5px solid var(--rule);
  }
  .bullet-list {
    position: absolute;
    list-style: none;
    font-family: "Arimo", Arial, sans-serif;
    font-size: 14.5px;
    line-height: 23.5px;
  }
  .bullet-list li::before { content: "\2666"; font-size: 11px; margin-right: 4px; position: relative; top: -1px; }
  .bullet-list .sub { padding-left: 34px; }

  .product-photo { position: absolute; }

  .about-box {
    position: absolute; left: 445px; top: 86px; width: 300px; height: 257px;
    background: var(--green);
    padding: 14px 14px 0 8px;
    font-family: "Arimo", Arial, sans-serif;
    font-size: 17.2px; line-height: 25.7px; color: #000;
  }

  .contact-box {
    position: absolute; left: 846px; top: 421px; width: 308px; height: 409px;
    background: var(--green);
    padding: 18px 0 0 22px;
    font-family: "Crimson Text", "Palatino Linotype", serif;
    color: #000;
  }
  .contact-box h2 {
    font-family: "Didact Gothic", "Century Gothic", sans-serif;
    font-weight: 400; font-size: 34px; line-height: 1; margin-bottom: 18px;
  }
  .contact-address { font-weight: 700; font-size: 19.5px; line-height: 23px; margin-bottom: 12px; }
  .contact-line { font-size: 17px; line-height: 24.5px; white-space: nowrap; }
  .contact-line b { font-size: 18px; }
  .hours-title { font-weight: 700; font-size: 21px; text-decoration: underline; margin-top: 10px; line-height: 27px; }
  .hours-line { font-size: 16.5px; line-height: 23.5px; white-space: nowrap; }
  .hours-line b { font-size: 18px; }

  .brand-signoff {
    position: absolute; left: 22px; right: 22px; bottom: 12px;
    padding-top: 6px;
    border-top: 1px solid #000;
  }
  .brand-name { font-weight: 700; font-size: 20px; line-height: 24px; }
  .brand-tagline { font-size: 15.5px; line-height: 20px; white-space: nowrap; }
</style>
</head>
<body>
<main class="brochure">

  <svg class="product-photo" style="left:73px; top:49px;" width="208" height="368" role="img" aria-label="Photo of an engraved glass award plaque on a black metal stand">
    <defs>
      <linearGradient id="plaqueTone" x1="0" y1="0" x2="1" y2="1">
        <stop offset="0" stop-color="#2d3a6a"/>
        <stop offset="0.5" stop-color="#141820"/>
        <stop offset="1" stop-color="#3a4a38"/>
      </linearGradient>
    </defs>
    <rect x="10" y="0" width="180" height="270" fill="url(#plaqueTone)"/>
    <rect x="0" y="275" width="200" height="93" fill="#1e1e1e"/>
  </svg>

  <h2 class="section-title" style="left:47px; top:444px; width:296px;">Products:</h2>
  <ul class="bullet-list" style="left:53px; top:504px;">
    <li>Laser Engraving</li>
    <li>Trophies</li>
    <li>Plaques</li>
    <li>Crystal, Glass &amp; Acrylic Awards</li>
    <li>Clocks</li>
    <li>Frames</li>
    <li>Customized Stamps</li>
    <li>Name Badges, Signs &amp; Holders</li>
    <li>Plastic Signage</li>
    <li>Medals &amp; Ribbons</li>
    <li>Cast Bronze &amp; Silver Tablets</li>
    <li>Screen Printing &amp; Embroidery</li>
    <li>Advertising Specialties:</li>
    <li class="sub">Mugs, Pens, Magnets &amp; More!</li>
  </ul>

  <h2 class="section-title" style="left:445px; top:45px; width:300px;">About Us:</h2>
  <div class="about-box">Since 1983 our staff has been creating quality engraved awards, trophies, and plaques along with a full line of promotional products and embroidered apparel. We continue to offer top quality workmanship on a wide range of products and as always, you will receive our outstanding personal service.</div>

  <h2 class="section-title" style="left:445px; top:358px; width:300px;">Choices:</h2>
  <ul class="bullet-list" style="left:452px; top:416px;">
    <li>Achievement Awards</li>
    <li>Recognition Awards</li>
    <li>Boss Gift Awards</li>
    <li>Employee Awards</li>
    <li>Executive Gift Awards</li>
    <li>Golf Awards</li>
    <li>Religious Awards</li>
    <li>Sales Awards</li>
    <li>Secretary Gift Awards</li>
    <li>Scholastic Achievement</li>
    <li>Athletic Milestones</li>
    <li>Personalized Gifts</li>
  </ul>

  <h2 class="section-title" style="left:452px; top:708px; width:293px;">We Provide:</h2>
  <ul class="bullet-list" style="left:452px; top:767px;">
    <li>Customer Service</li>
    <li>Rush Service</li>
    <li>Fast Turnaround</li>
    <li>Free Proofs</li>
    <li>Shipping Anywhere in the United States</li>
  </ul>

  <svg class="product-photo" style="left:873px; top:59px;" width="281" height="334" role="img" aria-label="Photo of a gold three-star trophy on a mahogany base">
    <defs>
      <radialGradient id="trophyTone" cx="0.4" cy="0.35" r="0.7">
        <stop offset="0" stop-color="#f2d36a"/>
        <stop offset="0.5" stop-color="#c9a041"/>
        <stop offset="1" stop-color="#f2f2f2"/>
      </radialGradient>
    </defs>
    <rect x="0" y="0" width="281" height="230" fill="url(#trophyTone)"/>
    <rect x="10" y="230" width="180" height="104" fill="#5e1d1b"/>
  </svg>

  <section class="contact-box">
    <h2>Contact Us:</h2>
    <p class="contact-address">4182 Dorrance Mill Road<br>Easton, PA 18045</p>
    <p class="contact-line"><b>Phone:</b> (610) 555-0147</p>
    <p class="contact-line"><b>Fax:</b> (610) 555-0193</p>
    <p class="contact-line"><b>Email:</b> sales@kestrelawards.example</p>
    <p class="contact-line"><b>Web:</b> www.kestrelawards.example</p>
    <p class="hours-title">Hours of Operation:</p>
    <p class="hours-line"><b>Mon-Wed-Fri:</b> 9am – 6pm</p>
    <p class="hours-line"><b>Tues-Thurs:</b> 9am – 7pm</p>
    <p class="hours-line"><b>Sat:</b> 9am – 4pm (May-Aug until 2pm)</p>
    <div class="brand-signoff">
      <p class="brand-name">Kestrel Trophy &amp; Awards</p>
      <p class="brand-tagline">Recognition at its best · 30 Years in Business</p>
    </div>
  </section>

</main>
</body>
</html>
```